Brightwater Residential Holdings Business Card Design - Logo Provided

business card design - LOGO PROVIDED. private capital fund investing in: commercial real estate (apartments), asset backed lending, private credit, flexible capital

Target Market(s)

private capital: commercial real estate (apartments), asset backed lending, private credit, flexible capital

Industry/Entity Type

alternative asset management

Contact Information for Business Card

logo, name, title, phone number, email and website

Font styles to use
Sans Serif

Colors
0054AA
0677BA
7BADD7
CADEEF
E8F1F8
EB3D1F
EC4F4E
F09395
F8D3D4
FCEDEE

Requirements
Must have
• use of logo on both sides and a qr code on the back

```html
<!DOCTYPE html>
<html lang="en">
<head>
<meta charset="utf-8">
<title>Brightwater Residential Holdings – Business Card</title>
<link href="https://fonts.googleapis.com/css2?family=Lato:wght@400;700;900&display=swap" rel="stylesheet">
<style>
  :root {
    --backdrop: #161616;
    --navy: #25397a;
    --navy-deep: #1f2f68;
    --navy-light: #2c4391;
    --red: #d9232d;
    --red-light: #ef3a41;
    --paper: #ebebeb;
    --ink: #1b1b1b;
    --white: #ffffff;
    --qr-fill: #d2d2d2;
  }
  * { box-sizing: border-box; margin: 0; padding: 0; }
  html, body { width: 1200px; height: 1000px; overflow: hidden; }
  body {
    background: var(--backdrop);
    font-family: "Lato", sans-serif;
    position: relative;
  }
  .card {
    position: absolute;
    left: 223px;
    width: 755px;
    height: 432px;
    border-radius: 28px;
    overflow: hidden;
  }
  .card--front {
    top: 56px;
    background: radial-gradient(ellipse at 40% 30%, var(--navy-light) 0%, var(--navy) 55%, var(--navy-deep) 100%);
  }
  .card--back {
    top: 512px;
    height: 431px;
    background: var(--paper);
  }
  .edge-band {
    position: absolute;
    left: 67px;
    width: 618px;
    bottom: 0;
    height: 10px;
    border-radius: 10px 10px 0 0;
  }
  .card--front .edge-band { background: linear-gradient(90deg, var(--red), var(--red-light), var(--red)); }
  .card--back .edge-band { background: linear-gradient(90deg, var(--navy-deep), #3a55a8, var(--navy-deep)); }

  .brand {
    position: absolute;
    display: flex;
    align-items: center;
    gap: 12px;
    font-weight: 900;
    text-transform: uppercase;
    line-height: 1.05;
    letter-spacing: 0.5px;
  }
  .brand__square { width: 26px; height: 26px; background: var(--red); flex: none; }
  .brand__name { font-size: 24px; }
  .card--front .brand { left: 290px; top: 172px; color: var(--white); }
  .card--back .brand { left: 470px; top: 148px; color: var(--navy); }

  .corner-mark {
    position: absolute;
    right: 32px;
    bottom: 60px;
    width: 22px;
    height: 22px;
    background: var(--red);
  }
  .web {
    position: absolute;
    right: 83px;
    bottom: 37px;
    display: flex;
    align-items: center;
    gap: 8px;
    color: var(--white);
    font-size: 15px;
    font-weight: 700;
  }

  .identity { position: absolute; left: 54px; top: 72px; }
  .identity__name { color: var(--red); font-size: 36px; font-weight: 900; letter-spacing: -0.3px; line-height: 1; }
  .identity__title { color: var(--ink); font-size: 18px; margin-top: 3px; }

  .contacts { position: absolute; left: 58px; top: 174px; list-style: none; color: var(--ink); font-size: 18px; font-weight: 700; }
  .contacts li { display: flex; align-items: flex-start; gap: 11px; margin-bottom: 13px; line-height: 24px; }
  .contacts li:nth-child(2) { margin-bottom: 17px; }
  .contacts svg { flex: none; margin-top: 4px; }

  .divider-line {
    position: absolute;
    left: 336px;
    top: 66px;
    width: 1px;
    height: 314px;
    background: linear-gradient(180deg, rgba(0,0,0,0), rgba(0,0,0,0.12) 20%, rgba(0,0,0,0.12) 80%, rgba(0,0,0,0));
  }
  .divider-shadow {
    position: absolute;
    left: 337px;
    top: 80px;
    width: 60px;
    height: 290px;
    background: radial-gradient(ellipse 100% 50% at 0% 50%, rgba(0,0,0,0.12), rgba(0,0,0,0) 100%);
    filter: blur(6px);
  }

  .qr-placeholder {
    position: absolute;
    left: 483px;
    top: 290px;
    width: 64px;
    height: 64px;
    background: var(--qr-fill);
    border-radius: 4px;
  }
</style>
</head>
<body>

  <section class="card card--front">
    <div class="brand">
      <span class="brand__square"></span>
      <span class="brand__name">Brightwater<br>Residential<br>Holdings</span>
    </div>
    <div class="web">
      <svg width="16" height="16" viewBox="0 0 16 16" aria-hidden="true"><circle cx="8" cy="8" r="7" fill="none" stroke="#d9232d" stroke-width="1.6"/><ellipse cx="8" cy="8" rx="3" ry="7" fill="none" stroke="#d9232d" stroke-width="1.4"/><line x1="1" y1="8" x2="15" y2="8" stroke="#d9232d" stroke-width="1.4"/></svg>
      www.brightwaterrh.com
    </div>
    <span class="corner-mark"></span>
    <div class="edge-band"></div>
  </section>

  <section class="card card--back">
    <div class="identity">
      <h1 class="identity__name">CLARA HOLLIS</h1>
      <p class="identity__title">Managing Director</p>
    </div>
    <ul class="contacts">
      <li>
        <svg width="17" height="17" viewBox="0 0 24 24" aria-hidden="true"><path fill="#25397a" d="M6.6 10.8a15 15 0 0 0 6.6 6.6l2.2-2.2c.3-.3.7-.4 1-.2 1.1.4 2.3.6 3.6.6.6 0 1 .4 1 1V20c0 .6-.4 1-1 1A17 17 0 0 1 3 4c0-.6.4-1 1-1h3.5c.6 0 1 .4 1 1 0 1.3.2 2.5.6 3.6.1.3 0 .7-.2 1z"/></svg>
        044-555 210 348
      </li>
      <li>
        <svg width="17" height="15" viewBox="0 0 24 20" aria-hidden="true"><rect x="1" y="2" width="22" height="16" rx="2" fill="#25397a"/><path d="M2 4l10 7 10-7" fill="none" stroke="#ebebeb" stroke-width="2"/></svg>
        info@brightwaterrh.com
      </li>
      <li>
        <svg width="15" height="19" viewBox="0 0 20 26" aria-hidden="true"><path fill="#25397a" d="M10 0a9 9 0 0 0-9 9c0 7 9 17 9 17s9-10 9-17a9 9 0 0 0-9-9zm0 12.5A3.5 3.5 0 1 1 10 5.5a3.5 3.5 0 0 1 0 7z"/></svg>
        <span>412 Harbor Ln<br>Lakeview, FL 33520,<br>2750 Pine Crest Way<br>Coral Bay, FL 33915</span>
      </li>
    </ul>
    <div class="divider-shadow"></div>
    <div class="divider-line"></div>
    <div class="brand">
      <span class="brand__square"></span>
      <span class="brand__name">Brightwater<br>Residential<br>Holdings</span>
    </div>
    <div class="qr-placeholder" role="img" aria-label="QR code linking to the company website"></div>
    <div class="edge-band"></div>
  </section>

</body>
</html>
```